Bright Harbor Construction

We are a commercial construction company specializing in steel stud framing, drywall, taping and acoustical ceilings. We would like a company logo (Something that looks great and isnt boring) as we have not been able to come up with one. A modern looking card would definitely suit our personalities best

We would like to try and avoid using dark colors. I have learned from experience that dark colors are the last to looked at. Thank you

```html
<!DOCTYPE html>
<html lang="en">
<head>
<meta charset="utf-8">
<title>Bright Harbor Construction – Business Card</title>
<link href="https://fonts.googleapis.com/css2?family=Montserrat:wght@400;500;700&display=swap" rel="stylesheet">
<style>
  :root {
    --backdrop: #e4e4e4;
    --card-top: #f1f1f1;
    --card-base: #ffffff;
    --accent: #ffcc00;
    --accent-deep: #ff9a00;
    --name-amber: #e59a00;
    --text-strong: #2e2e2e;
    --text-muted: #5a5a5a;
    --photo-warm: #f7d88e;
    --photo-soft: #f3e6cc;
  }
  * { box-sizing: border-box; margin: 0; padding: 0; }
  html, body { width: 1200px; height: 900px; overflow: hidden; }
  body {
    background: var(--backdrop);
    font-family: "Montserrat", sans-serif;
    position: relative;
  }
  .card {
    position: absolute;
    top: 150px;
    width: 366px;
    height: 600px;
    overflow: hidden;
    box-shadow: 0 6px 18px rgba(0, 0, 0, 0.12);
  }
  .card--front { left: 186px; }
  .card--back { left: 651px; }
  .card__art { position: absolute; inset: 0; width: 100%; height: 100%; }

  .brand {
    position: absolute;
    left: 0; right: 0;
    text-align: center;
    color: var(--text-strong);
    font-weight: 500;
    letter-spacing: -0.3px;
  }
  .brand__mark {
    display: block;
    margin: 0 auto 8px;
    border-radius: 50%;
    background: var(--text-strong);
  }
  .card--front .brand { top: 42px; font-size: 18px; }
  .card--front .brand__mark { width: 34px; height: 34px; }
  .card--back .brand { top: 236px; font-size: 26px; line-height: 1.2; }
  .card--back .brand__mark { width: 46px; height: 46px; margin-bottom: 12px; }

  .holder {
    position: absolute;
    left: 0; right: 0;
    top: 214px;
    text-align: center;
  }
  .holder__name {
    color: var(--name-amber);
    font-weight: 700;
    font-size: 24px;
    letter-spacing: -0.5px;
  }
  .holder__role {
    color: var(--text-muted);
    font-weight: 700;
    font-size: 17px;
    margin-top: 2px;
  }

  .contacts {
    position: absolute;
    left: 44px;
    top: 391px;
    list-style: none;
  }
  .contacts__item {
    display: flex;
    align-items: center;
    height: 29.5px;
    color: var(--text-muted);
    font-size: 19px;
    white-space: nowrap;
  }
  .contacts__icon { width: 25px; height: 25px; margin-right: 13px; flex: none; }

  .back-url {
    position: absolute;
    left: 0; right: 0;
    top: 552px;
    text-align: center;
    color: var(--name-amber);
    font-size: 18px;
    font-weight: 500;
  }
</style>
</head>
<body>

<section class="card card--front">
  <svg class="card__art" viewBox="0 0 610 1000" preserveAspectRatio="none">
    <defs>
      <linearGradient id="accentFade" x1="0" y1="0" x2="0" y2="1">
        <stop offset="0.55" stop-color="#ffcc00"/>
        <stop offset="1" stop-color="#ff9a00"/>
      </linearGradient>
    </defs>
    <rect width="610" height="1000" fill="#f1f1f1"/>
    <polygon points="170,240 610,335 610,1000 0,1000 0,478" fill="#ffffff"/>
    <polygon points="0,202 170,240 0,478" fill="url(#accentFade)"/>
    <polygon points="610,805 610,1000 475,1000" fill="url(#accentFade)"/>
  </svg>

  <div class="brand"><span class="brand__mark"></span>Bright Harbor Construction</div>

  <div class="holder">
    <p class="holder__name">YOUR NAME</p>
    <p class="holder__role">POSITION</p>
  </div>

  <ul class="contacts">
    <li class="contacts__item">
      <svg class="contacts__icon" viewBox="0 0 24 24"><circle cx="12" cy="12" r="12" fill="#ffb400"/><path d="M8 7l2 2-1.2 1.6c.8 1.6 2 2.8 3.6 3.6L14 13l2 2-1.6 2C10 16.4 7.6 14 7 9.6z" fill="#2e2e2e"/></svg>
      +000 1234567
    </li>
    <li class="contacts__item">
      <svg class="contacts__icon" viewBox="0 0 24 24"><circle cx="12" cy="12" r="12" fill="#ffb400"/><rect x="6" y="8" width="12" height="8.5" fill="none" stroke="#2e2e2e" stroke-width="1.4"/><path d="M6 8l6 5 6-5M6 16.5l4.5-4.3M18 16.5l-4.5-4.3" fill="none" stroke="#2e2e2e" stroke-width="1.2"/></svg>
      you@brightharbor.com
    </li>
    <li class="contacts__item">
      <svg class="contacts__icon" viewBox="0 0 24 24"><circle cx="12" cy="12" r="12" fill="#ffb400"/><g fill="none" stroke="#2e2e2e" stroke-width="1.1"><circle cx="12" cy="12" r="6.5"/><ellipse cx="12" cy="12" rx="3" ry="6.5"/><path d="M5.5 12h13M6.5 8.8h11M6.5 15.2h11M12 5.5v13"/></g></svg>
      www.yourcompany.com
    </li>
    <li class="contacts__item">
      <svg class="contacts__icon" viewBox="0 0 24 24"><circle cx="12" cy="12" r="12" fill="#ffb400"/><path d="M12 19s-5-5.2-5-8.8a5 5 0 0 1 10 0C17 13.8 12 19 12 19z" fill="#2e2e2e"/><circle cx="12" cy="10.2" r="2" fill="#ffb400"/></svg>
      your address here
    </li>
  </ul>
</section>

<section class="card card--back">
  <svg class="card__art" viewBox="0 0 610 1000" preserveAspectRatio="none">
    <defs>
      <linearGradient id="cityGlow" x1="0" y1="0" x2="0.3" y2="1">
        <stop offset="0" stop-color="#f7d88e"/>
        <stop offset="0.45" stop-color="#f5e0b0"/>
        <stop offset="1" stop-color="#f3e6cc"/>
      </linearGradient>
    </defs>
    <rect width="610" height="1000" fill="#f1f1f1"/>
    <polygon points="0,185 610,52 610,948 0,815" fill="url(#cityGlow)" role="img" aria-label="Photo of a city skyline with tall towers at sunset"/>
  </svg>

  <div class="brand"><span class="brand__mark"></span>Bright Harbor<br>Construction</div>

  <p class="back-url">www.yourcompany.com</p>
</section>

</body>
</html>
```